K & D A/C Compressors' Business Card

Hello,

I need someone to create a new business card for my business. The name of my Business is: K & D A/C Compressors. I sell automotive air conditioning parts (a/c parts). I would like the business card to incorporate my logo, and to have an automotive feel to it. It is important that the business card feel like it is coming from an automotive parts business.

I already have a logo, which I will provide.

Thanks.
Updates

Project Deadline Extended Reason: I feel like extending the deadline until October 9, 2017, will allow for more time to design the business card. Thank you for your understanding. Added Monday, October 2, 2017

Target Market(s)

Consumers who need automotive a/c parts, and auto mechanics.

Industry/Entity Type

Automotive

Contact Information for Business Card

Business name: K & D A/C Compressors
Business Address: 48207 Southwest 36th Street, Palm Crest, Georgia 30599
Telephone: 305-472-1390
Fax: To be provided once I choose your design.
Website: www.kdcoolunits.example
Email: support@kdcoolunits.example
Names: To be provided once I choose your design.

Font styles to use
Sans Serif

Colors

Designer to choose colors to be used in the design.

Requirements
Must have
• The business card must include all of the "Business Card Details" and the logo I have uploaded.

```html
<!DOCTYPE html>
<html lang="en">
<head>
<meta charset="utf-8">
<title>K &amp; D A/C Compressors – Business Card</title>
<link rel="stylesheet" href="https://fonts.googleapis.com/css2?family=Roboto:wght@400&display=swap">
<style>
  :root {
    --page-bg: #ececec;
    --card-black: #000000;
    --card-white: #ffffff;
    --brand-blue: #009fe3;
    --brand-grey: #b3b3b3;
    --text-light: #ffffff;
  }
  * { margin: 0; padding: 0; box-sizing: border-box; }
  html, body {
    width: 1200px; height: 1000px; overflow: hidden;
    background: var(--page-bg);
    font-family: "Roboto", Arial, sans-serif;
  }
  .canvas { position: relative; width: 1200px; height: 1000px; }
  .card { position: absolute; left: 276px; width: 648px; overflow: hidden; }
  .card-front { top: 92px; height: 370px; }
  .card-back { top: 538px; height: 369px; }
  .card-art { position: absolute; inset: 0; }

  .brand-name {
    position: absolute; color: var(--brand-grey); font-weight: 400; line-height: 1;
    display: flex; flex-direction: column;
  }
  .brand-name .line-main { letter-spacing: 3px; }
  .card-front .brand-name { left: 198px; top: 150px; }
  .card-front .line-main { font-size: 46px; }
  .card-front .line-sub { font-size: 22px; margin-top: 6px; letter-spacing: 0.5px; }
  .card-back .brand-name { left: 184px; top: 60px; }
  .card-back .line-main { font-size: 56px; }
  .card-back .line-sub { font-size: 28px; margin-top: 10px; letter-spacing: 0.5px; }

  .person { position: absolute; left: 0; top: 238px; width: 207px; color: var(--text-light); }
  .person-name { display: flex; align-items: center; gap: 8px; padding-left: 8px; font-size: 23px; }
  .person-rule { margin-top: 10px; height: 7px; border-top: 2px solid var(--text-light); border-bottom: 2px solid var(--text-light); }
  .person-title { margin-top: 8px; text-align: center; font-size: 13px; }
  .person-mobile { display: flex; align-items: center; gap: 12px; margin-top: 24px; padding-left: 12px; font-size: 13px; }

  .contact-list { position: absolute; left: 390px; top: 231px; list-style: none; color: var(--text-light); font-size: 12.5px; }
  .contact-list li { display: flex; align-items: flex-start; gap: 12px; height: 28.5px; }
  .contact-list li.address { line-height: 16px; }
  .contact-list svg { flex: none; }
</style>
</head>
<body>
<div class="canvas">

  <section class="card card-front" aria-label="Business card front">
    <svg class="card-art" viewBox="0 0 648 370" width="648" height="370" aria-hidden="true">
      <rect width="648" height="370" fill="var(--card-black)"/>
      <rect y="54" width="648" height="3" fill="var(--card-white)"/>
      <rect y="60" width="648" height="3" fill="var(--card-white)"/>
      <rect y="66" width="648" height="3" fill="var(--card-white)"/>
      <rect y="133" width="648" height="103" fill="var(--card-white)"/>
      <polygon points="0,133 257,133 0,236" fill="var(--brand-blue)"/>
      <polygon points="0,236 96,215 199,236" fill="var(--brand-blue)"/>
      <rect y="289" width="648" height="3" fill="var(--card-white)"/>
      <rect y="295" width="648" height="3" fill="var(--card-white)"/>
      <rect y="301" width="648" height="3" fill="var(--card-white)"/>
    </svg>
    <div class="brand-name"><span class="line-main">K &amp; D</span><span class="line-sub">A/C Compressors</span></div>
  </section>

  <section class="card card-back" aria-label="Business card back">
    <svg class="card-art" viewBox="0 0 648 369" width="648" height="369" aria-hidden="true">
      <rect width="648" height="369" fill="var(--card-black)"/>
      <rect width="648" height="177" fill="var(--card-white)"/>
      <polygon points="0,0 257,0 7,178 0,178" fill="var(--brand-blue)"/>
      <polygon points="7,178 96,143 190,178" fill="var(--brand-blue)"/>
      <rect y="191" width="648" height="3" fill="var(--card-white)"/>
      <rect y="199" width="648" height="3" fill="var(--card-white)"/>
      <rect y="207" width="648" height="3" fill="var(--card-white)"/>
    </svg>
    <div class="brand-name"><span class="line-main">K &amp; D</span><span class="line-sub">A/C Compressors</span></div>

    <div class="person">
      <div class="person-name">
        <svg width="20" height="22" viewBox="0 0 20 22" aria-hidden="true"><circle cx="10" cy="6" r="5.5" fill="var(--brand-blue)"/><path d="M0 22c0-7 4-10 10-10s10 3 10 10z" fill="var(--brand-blue)"/></svg>
        <span>Mark Delano</span>
      </div>
      <div class="person-rule"></div>
      <div class="person-title">Director</div>
      <div class="person-mobile">
        <svg width="10" height="22" viewBox="0 0 10 22" aria-hidden="true"><rect x="0" y="3" width="10" height="19" rx="1.5" fill="var(--brand-blue)"/><rect x="2" y="0" width="1.5" height="4" fill="var(--brand-blue)"/><rect x="2" y="6" width="6" height="4" fill="var(--card-black)"/></svg>
        <span>305-472-1390</span>
      </div>
    </div>

    <ul class="contact-list">
      <li>
        <svg width="20" height="18" viewBox="0 0 20 18" aria-hidden="true"><rect x="4" y="0" width="12" height="6" fill="var(--brand-blue)"/><rect x="0" y="7" width="20" height="11" rx="2" fill="var(--brand-blue)"/><rect x="5" y="10" width="10" height="3" fill="var(--card-black)"/></svg>
        <span>305-472-1390</span>
      </li>
      <li>
        <svg width="18" height="18" viewBox="0 0 18 18" aria-hidden="true"><text x="9" y="14" text-anchor="middle" font-family="Roboto, sans-serif" font-size="17" fill="var(--brand-blue)">@</text></svg>
        <span>support@kdcoolunits.example</span>
      </li>
      <li>
        <svg width="18" height="18" viewBox="0 0 18 18" aria-hidden="true" fill="none" stroke="var(--brand-blue)" stroke-width="1.6"><circle cx="9" cy="9" r="8"/><ellipse cx="9" cy="9" rx="3.5" ry="8"/><path d="M1 9h16M2.5 5h13M2.5 13h13"/></svg>
        <span>www.kdcoolunits.example</span>
      </li>
      <li class="address">
        <svg width="18" height="16" viewBox="0 0 18 16" aria-hidden="true"><path d="M9 0 0 8h3v8h4v-5h4v5h4V8h3z" fill="var(--brand-blue)"/></svg>
        <span>48207 Southwest 36th Street,<br>Palm Crest, Georgia 30599</span>
      </li>
    </ul>
  </section>

</div>
</body>
</html>
```